Business Card Design for Real Estate Company

I am looking for a business card design that will catch my client's attention.

Industry/Entity Type

Business

Requirements
Must have
• Please have the following information in the business card design. You can substitute the "Office, Mobile, email, and web" with an icon or some other design you may think will go well with the business card.

Toma Verdi
482 W. Orchard Blvd., Suite 300
Pasadena, CA 91187
Office: 626.555.0147
Mobile: 626.555.0193
email: Toma@QuillStoneEstates.example
web: www.QuillStoneEstates.example

```html
<!DOCTYPE html>
<html lang="en">
<head>
<meta charset="utf-8">
<title>Quill Stone Estates – Business Card</title>
<link href="https://fonts.googleapis.com/css2?family=Cabin:wght@400;500&display=swap" rel="stylesheet">
<style>
  :root {
    --backdrop: #2b2b2d;
    --card: #ffffff;
    --card-shade: #f1f1f1;
    --brand-brown: #5b4630;
    --brand-blue: #1d5a99;
    --band-blue: #0f4c8c;
    --band-text: #b9d4ef;
    --ink: #333333;
    --leaf-blue: #4f8fc9;
  }
  html, body {
    margin: 0;
    padding: 0;
    width: 1200px;
    height: 900px;
    overflow: hidden;
    background: var(--backdrop);
    font-family: "Cabin", "Gill Sans", sans-serif;
  }
  .canvas {
    position: relative;
    width: 1200px;
    height: 900px;
  }
  .card {
    position: absolute;
    left: 320px;
    width: 560px;
    height: 320px;
    border-radius: 24px;
    background: linear-gradient(180deg, var(--card) 0%, var(--card-shade) 100%);
    overflow: hidden;
    box-shadow: 0 10px 30px rgba(0,0,0,0.45);
    box-sizing: border-box;
  }
  .card--front {
    top: 110px;
    display: flex;
    align-items: center;
    justify-content: space-between;
    gap: 32px;
    padding: 0 44px 0 50px;
  }
  .card--back  { top: 470px; }

  /* Front */
  .front-mark {
    flex: none;
    width: 150px;
    height: 150px;
    border-radius: 50%;
    background: var(--leaf-blue);
  }
  .front-name {
    margin: 0;
    font-size: 34px;
    font-weight: 400;
    color: var(--brand-brown);
    letter-spacing: 0.3px;
    white-space: nowrap;
  }

  /* Back */
  .brand {
    position: absolute;
    right: 40px;
    top: 60px;
    display: flex;
    align-items: center;
    gap: 12px;
  }
  .brand-dot {
    width: 22px;
    height: 22px;
    border-radius: 50%;
    background: var(--leaf-blue);
  }
  .brand-name {
    margin: 0;
    font-size: 30px;
    font-weight: 400;
    color: var(--brand-brown);
  }
  .person {
    position: absolute;
    left: 40px;
    top: 170px;
  }
  .person-name {
    margin: 0 0 10px;
    font-size: 22px;
    font-weight: 500;
    font-variant: small-caps;
    letter-spacing: 1px;
    color: var(--brand-blue);
  }
  .contact-line {
    display: flex;
    align-items: center;
    gap: 8px;
    font-size: 17px;
    color: var(--ink);
    margin: 0 0 4px;
  }
  .icon { width: 14px; height: 14px; flex: none; }
  .online {
    position: absolute;
    right: 40px;
    top: 180px;
    text-align: right;
  }
  .online .contact-line { justify-content: flex-end; font-size: 15px; }
  .band {
    position: absolute;
    left: 0;
    bottom: 0;
    width: 100%;
    height: 58px;
    background: var(--band-blue);
    display: flex;
    align-items: center;
    justify-content: flex-end;
    padding-right: 40px;
    box-sizing: border-box;
  }
  .address {
    margin: 0;
    font-size: 15px;
    color: var(--band-text);
    letter-spacing: 0.5px;
  }
</style>
</head>
<body>
<main class="canvas">

  <section class="card card--front" aria-label="Card front">
    <div class="front-mark"></div>
    <h1 class="front-name">Quill Stone Estates</h1>
  </section>

  <section class="card card--back" aria-label="Card back">
    <div class="brand">
      <span class="brand-dot"></span>
      <h2 class="brand-name">Quill Stone Estates</h2>
    </div>

    <div class="person">
      <h3 class="person-name">Toma Verdi</h3>
      <p class="contact-line">
        <svg class="icon" viewBox="0 0 16 16" aria-label="Office">
          <path d="M4 1.5l2.2 3-1.3 1.6c.8 1.8 2.2 3.2 4 4l1.6-1.3 3 2.2-1.3 2.5C7.6 14 2 8.4 1.5 3z" fill="var(--ink)"/>
        </svg>
        626.555.0147
      </p>
      <p class="contact-line">
        <svg class="icon" viewBox="0 0 16 16" aria-label="Mobile">
          <rect x="4" y="1" width="8" height="14" rx="1.5" fill="none" stroke="var(--ink)" stroke-width="1.6"/>
          <circle cx="8" cy="12.5" r="0.9" fill="var(--ink)"/>
        </svg>
        626.555.0193
      </p>
    </div>

    <div class="online">
      <p class="contact-line">
        Toma@QuillStoneEstates.example
        <svg class="icon" viewBox="0 0 16 16" aria-label="Email">
          <rect x="1" y="3" width="14" height="10" rx="1" fill="var(--brand-blue)"/>
          <path d="M1.5 3.8L8 9l6.5-5.2" fill="none" stroke="#ffffff" stroke-width="1.2"/>
        </svg>
      </p>
      <p class="contact-line">
        www.QuillStoneEstates.example
        <svg class="icon" viewBox="0 0 16 16" aria-label="Web">
          <circle cx="8" cy="8" r="6.5" fill="var(--brand-blue)"/>
          <path d="M1.5 8h13M8 1.5c-3 3.5-3 9.5 0 13M8 1.5c3 3.5 3 9.5 0 13" fill="none" stroke="#ffffff" stroke-width="0.9"/>
        </svg>
      </p>
    </div>

    <div class="band">
      <p class="address">482 W. Orchard Blvd., Suite 300, Pasadena, CA 91187</p>
    </div>
  </section>

</main>
</body>
</html>
```